Flyer-Design für Bauträgerfirma
Zielgruppe
Wir sind eine Bauträgerfirma und bauen überwiegend hochwertige Neubauwohnungen.
Aufgabenstellung
Das Design sollte sehr professionell aussehen, nicht verspielt.
Im Anhang habe ich mal ein aktuelles PDF (Magazin für ein Projekt) und ein Faltflyer zum Mitnehmen hochgeladen.
Ebenso habe ich Ihnen auch zwei Beispiele von ansässigen Bauträgern angehängt, ich finde das Design der beiden Bauträger aber schrecklich, soll nur als Beispiel dienen, was ich benötige.
Ich benötige konkret ein Verkaufsflyer für die Neubauwohnungen laut dem Magazin, es sollen auch bereits verkaufte Wohnungen, bereits reservierte Wohnungen und noch freie dargestellt werden. Beim Kauf einer Wohnung bis zum ... gibt es ein Bemusterungsgutschein oben drauf.
Bitte im Format A4 gefaltet gestalten.

```html
<!DOCTYPE html>
<html lang="de">
<head>
<meta charset="utf-8">
<title>Wohnresidenz am Lindenhof – Verkaufsflyer Varianten</title>
<link href="https://fonts.googleapis.com/css2?family=Open+Sans:ital,wght@0,400;0,600;0,700;1,600&display=swap" rel="stylesheet">
<style>
:root{
  --bg:#c9c9c9;
  --navy:#1b2a44;
  --bar:#8b9bb9;
  --bar-light:#a9b6cc;
  --red:#c8202b;
  --orange:#e8541e;
  --text:#2b2b2b;
  --white:#ffffff;
}
*{box-sizing:border-box;margin:0;padding:0}
html,body{width:1200px;height:3179px;overflow:hidden}
body{background:var(--bg);font-family:"Open Sans",Arial,sans-serif;color:var(--text);position:relative}

.variant-label{position:absolute;left:43px;width:52px;border-top:1px solid #333;padding-top:10px;font-size:22px;color:#222}
.spread{position:absolute;width:955px;height:676px;background:var(--white);box-shadow:4px 5px 8px rgba(0,0,0,.35);overflow:hidden}

.ph{position:absolute}
.ph-town{background:linear-gradient(180deg,#e7b36c 0%,#b8805a 35%,#7a5a4a 70%,#5b4a44 100%)}
.ph-house{background:linear-gradient(180deg,#bfd1e6 0%,#e9eef2 45%,#c9c9c5 70%,#7f9466 100%)}
.ph-room{background:linear-gradient(135deg,#d9d4cc 0%,#9e9890 50%,#5a5654 100%)}
.ph-bedroom{background:linear-gradient(90deg,#2e3440 0%,#6d7078 40%,#e2e0db 75%,#c7b8a2 100%)}
.ph-building{background:linear-gradient(180deg,#dfe7ec 0%,#f2f2f2 40%,#9aa4a8 70%,#5f7a45 100%)}

.title{font-size:12px;font-weight:600;color:var(--navy);text-transform:uppercase;padding-bottom:5px;border-bottom:1px solid var(--navy);white-space:nowrap}
.intro{font-size:7.2px;line-height:9.4px;color:#333}

/* left panel */
.panel-left{position:absolute;left:0;top:0;width:240px;height:676px}
.panel-left .ph-town{left:0;top:0;width:240px;height:118px}
.band{position:absolute;left:0;top:118px;width:240px;height:11px;background:var(--bar-light)}
.left-copy{position:absolute;left:26px;top:156px;width:192px}
.left-copy .intro{margin-top:11px}
.tagline{margin-top:9px;font-size:8px;font-weight:600;font-style:italic;color:var(--navy)}
.navy-left{position:absolute;left:0;top:372px;width:240px;height:304px;background:var(--navy)}
.panel-left .big{left:25px;top:330px;width:190px;height:106px}
.panel-left .s1{left:25px;top:442px;width:93px;height:88px}
.panel-left .s2{left:122px;top:442px;width:93px;height:88px}
.panel-left .wide{left:25px;top:536px;width:190px;height:93px}
.claim{position:absolute;left:0;top:644px;width:240px;text-align:center;color:var(--white);font-size:9.6px}

/* middle panel */
.panel-mid{position:absolute;left:240px;top:0;width:476px;height:676px}
.mid-copy{position:absolute;left:24px;top:28px;width:200px}
.mid-copy .title{width:185px}
.mid-copy .intro{margin-top:8px}
.panel-mid .ph-bedroom{left:243px;top:16px;width:215px;height:100px}
.row{position:absolute;left:0;width:476px;height:170px}
.col{position:absolute;top:0;width:238px;height:170px}
.col.a{left:0}.col.b{left:238px}
.bar{position:absolute;left:3px;top:0;width:228px;height:24px;background:var(--bar);color:var(--white);font-size:12px;line-height:24px;padding-left:14px}
.bar .letter{position:absolute;right:8px;top:4px;width:16px;height:16px;border:1.3px solid var(--white);border-radius:50%;font-size:9px;line-height:14px;text-align:center}
.plan{position:absolute;left:20px;top:36px;width:128px;height:112px;background:linear-gradient(135deg,#c99a5e 0%,#e3c99b 35%,#8f7a62 60%,#2f3d5a 100%);border:2px solid #2f4a86}
.plan.out-orange{border-color:var(--orange)}
.tag{position:absolute;font-size:7px;color:var(--white);padding:1px 5px}
.tag.sold{background:var(--red)}
.tag.res{background:var(--orange)}
.nums{position:absolute;left:20px;top:151px;width:128px;display:flex;justify-content:space-around;font-size:6.8px;color:#333}
.units{position:absolute;left:160px;top:30px;width:70px;font-size:6.4px;line-height:8px;color:#333;text-align:right}
.unit{margin-bottom:2px}
.unit .name{border-bottom:1px solid #999;display:block}
.unit .st{color:var(--orange)}

/* right panel */
.panel-right{position:absolute;left:716px;top:0;width:239px;height:676px}
.panel-right .ph-building{left:0;top:0;width:239px;height:212px}
.navy-right{position:absolute;left:0;top:200px;width:239px;height:392px;background:var(--navy);padding:28px 22px 0 24px}
.navy-right .title{color:var(--white);border-color:var(--white);font-size:10.4px;line-height:14px;white-space:normal}
.reasons{list-style:none;margin-top:14px}
.reasons li{position:relative;padding-left:13px;color:#e6e9ef;font-size:6.5px;line-height:8px;margin-bottom:1.5px}
.reasons li::before{content:"";position:absolute;left:0;top:0.5px;width:7px;height:7px;background:var(--red)}
.reasons li::after{content:"";position:absolute;left:2.3px;top:1.3px;width:2px;height:3.6px;border:solid var(--white);border-width:0 1px 1px 0;transform:rotate(40deg)}
.action{position:absolute;left:40px;top:566px;width:170px;height:80px;background:var(--white);box-shadow:5px 5px 0 var(--red);text-align:center;padding-top:6px}
.action h3{font-size:13px;font-weight:600;color:var(--navy);margin-bottom:3px}
.action p{font-size:7.2px;line-height:9.4px;color:#333}
.v4 .action h3{text-transform:uppercase;color:var(--red)}
</style>
</head>
<body>

<div class="variant-label" style="top:86px">1</div>
<section class="spread" style="left:117px;top:86px">
  <div class="panel-left">
    <div class="ph ph-town" role="img" aria-label="Luftaufnahme der Stadt Talbrunn bei Sonnenuntergang"></div>
    <div class="band"></div>
    <div class="left-copy">
      <h2 class="title">Wohnresidenz am Lindenhof</h2>
      <p class="intro">In reizvoller Landschaft zwischen Schwarzwald, Bodensee, Schwäbischer Alb und Donautal liegt die kleine und lebendige Stadt Talbrunn. Hier bauen wir für Sie die "Wohnresidenz am Lindenhof": zwei hoch energieeffiziente Wohnhäuser mit FEB55 Standard und insgesamt 19 exklusiv ausgestatteten Wohnungen, umgeben von schönen Grünflächen und attraktiven Möglichkeiten für Einkauf und Freizeit im Nahbereich.</p>
      <p class="tagline">Geben Sie Ihre Träume in unsere Hände.</p>
    </div>
    <div class="navy-left"></div>
    <div class="ph ph-house big" role="img" aria-label="Außenansicht der Wohnanlage"></div>
    <div class="ph ph-room s1" role="img" aria-label="Wohnzimmer mit Essbereich"></div>
    <div class="ph ph-room s2" role="img" aria-label="Moderne Küche"></div>
    <div class="ph ph-room wide" role="img" aria-label="Helles Wohnzimmer mit Sofa"></div>
    <p class="claim">Wir definieren Wohnen neu.</p>
  </div>
  <div class="panel-mid">
    <div class="mid-copy">
      <h2 class="title">Sie haben die Wahl!</h2>
      <p class="intro">Die 19 Wohnungen der Wohnresidenz am Lindenhof bestehen aus 2 bis 4 Zimmern und sind von ca. 60 bis 160 Quadratmeter groß. Damit bietet das moderne Wohnprojekt geeigneten Wohnraum für Singles, für Pärchen sowie für Familien mit Kindern.</p>
    </div>
    <div class="ph ph-bedroom" role="img" aria-label="Schlafzimmer und offener Wohnbereich"></div>
    <div class="row" style="top:133px">
      <div class="col a"><div class="bar">Penthouse<span class="letter">A</span></div><div class="plan" role="img" aria-label="Grundriss Penthouse Haus A"><span class="tag sold" style="left:70px;top:8px">Verkauft</span></div><div class="nums"><span>107</span><span>108</span></div><div class="units"><p class="unit"><span class="name">Wohnung 107</span>~ 147,49 m²<br>987.654,32 €</p><p class="unit"><span class="name">Wohnung 108</span>~ 143,41 m²<br><span class="st">Verkauft</span></p></div></div>
      <div class="col b"><div class="bar">Penthouse<span class="letter">B</span></div><div class="plan out-orange" role="img" aria-label="Grundriss Penthouse Haus B"><span class="tag res" style="left:75px;top:12px">Reserviert</span></div><div class="nums"><span>209</span><span>210</span><span>211</span></div><div class="units"><p class="unit"><span class="name">Wohnung 209</span>~ 118,25 m²<br>987.654,32 €</p><p class="unit"><span class="name">Wohnung 210</span>~ 68,50 m²<br>987.654,32 €</p><p class="unit"><span class="name">Wohnung 211</span>~ 120,75 m²<br><span class="st">Reserviert</span></p></div></div>
    </div>
    <div class="row" style="top:299px">
      <div class="col a"><div class="bar">Obergeschoss<span class="letter">A</span></div><div class="plan" role="img" aria-label="Grundriss Obergeschoss Haus A"><span class="tag res" style="left:38px;top:92px">Reserviert</span></div><div class="nums"><span>104</span><span>105</span><span>106</span></div><div class="units"><p class="unit"><span class="name">Wohnung 104</span>~ 121,49 m²<br>987.654,32 €</p><p class="unit"><span class="name">Wohnung 105</span>~ 85,64 m²<br><span class="st">Reserviert</span></p><p class="unit"><span class="name">Wohnung 106</span>~ 123,32 m²<br>987.654,32 €</p></div></div>
      <div class="col b"><div class="bar">Obergeschoss<span class="letter">B</span></div><div class="plan" role="img" aria-label="Grundriss Obergeschoss Haus B"><span class="tag sold" style="left:82px;top:92px">Verkauft</span></div><div class="nums"><span>205</span><span>206</span><span>207</span><span>208</span></div><div class="units"><p class="unit"><span class="name">Wohnung 205</span>~ 121,49 m²<br>987.654,32 €</p><p class="unit"><span class="name">Wohnung 206</span>~ 60,20 m²<br>987.654,32 €</p><p class="unit"><span class="name">Wohnung 207</span>~ 60,20 m²<br><span class="st">Verkauft</span></p><p class="unit"><span class="name">Wohnung 208</span>~ 114,61 m²<br>987.654,32 €</p></div></div>
    </div>
    <div class="row" style="top:483px">
      <div class="col a"><div class="bar">Erdgeschoss<span class="letter">A</span></div><div class="plan" role="img" aria-label="Grundriss Erdgeschoss Haus A"><span class="tag sold" style="left:4px;top:10px">Verkauft</span></div><div class="nums"><span>101</span><span>102</span><span>103</span></div><div class="units"><p class="unit"><span class="name">Wohnung 101</span>~ 103,96 m²<br><span class="st">Verkauft</span></p><p class="unit"><span class="name">Wohnung 102</span>~ 85,64 m²<br>987.654,32 €</p><p class="unit"><span class="name">Wohnung 103</span>~ 109,02 m²<br>987.654,32 €</p></div></div>
      <div class="col b"><div class="bar">Erdgeschoss<span class="letter">B</span></div><div class="plan" role="img" aria-label="Grundriss Erdgeschoss Haus B"><span class="tag res" style="left:82px;top:10px">Reserviert</span></div><div class="nums"><span>201</span><span>202</span><span>203</span><span>204</span></div><div class="units"><p class="unit"><span class="name">Wohnung 201</span>~ 103,96 m²<br>987.654,32 €</p><p class="unit"><span class="name">Wohnung 202</span>~ 60,20 m²<br>987.654,32 €</p><p class="unit"><span class="name">Wohnung 203</span>~ 60,21 m²<br>987.654,32 €</p><p class="unit"><span class="name">Wohnung 204</span>~ 114,61 m²<br><span class="st">Reserviert</span></p></div></div>
    </div>
  </div>
  <div class="panel-right">
    <div class="ph ph-building" role="img" aria-label="Moderner Neubau mit Balkonen und Terrassen"></div>
    <div class="navy-right">
      <h2 class="title">Gründe für eine Wohnung der Wohnresidenz am Lindenhof</h2>
      <ul class="reasons">
        <li>Fenster mit Dreifachverglasung und einem optimalen Sonnenschutz</li>
        <li>Verlegung hochwertiger Bodenbeläge</li>
        <li>Fußbodenheizung mit Komfort-Einzelregelung</li>
        <li>Überhohe Türen von 2,12 m</li>
        <li>Verwendung bekannter Hersteller bei Sanitärprodukten wie Aquaris, Keramo oder Sanoro</li>
        <li>Barrierefreie, bodenebene Duschen</li>
        <li>Hochwertige Multimediastationen in jedem Wohnraum</li>
        <li>Elektrische Rollläden bzw. Jalousien</li>
        <li>Abstellmöglichkeit für 2 Fahrräder gegeben</li>
        <li>Überhohe Decken</li>
        <li>Niedrigenergiehaus als Effizienzhaus 55 gem. EnEV 2016 (ca. 45% besser als gefordert)</li>
        <li>Zinsgünstige Darlehen aufgrund FEB55 möglich (100.000.- € ab 0,75%)</li>
        <li>Staatlicher Zuschuss von 5.000.- €</li>
        <li>Barrierefreier Aufzug von der Tiefgarage bis in jede Wohnung</li>
        <li>Tiefgaragenstellplatz optional erhältlich</li>
        <li>Zukunftsweisende KNX/EIB Bus-Elektroinstallation möglich</li>
        <li>Kontrollierte Wohnraumbelüftung mit Wärmerückgewinnung in allen Wohnungen</li>
      </ul>
    </div>
    <div class="action"><h3>Aktion</h3><p>Beim Kauf einer Wohnung<br>bis zum XX.XX.XX, erhalten Sie<br>einen Bemusterungsgutschein<br>im Wert von 5.000 €.</p></div>
  </div>
</section>

<div class="variant-label" style="top:876px">2</div>
<section class="spread" style="left:125px;top:876px">
  <div class="panel-left">
    <div class="ph ph-town" role="img" aria-label="Luftaufnahme der Stadt Talbrunn bei Sonnenuntergang"></div>
    <div class="band"></div>
    <div class="left-copy">
      <h2 class="title">Wohnresidenz am Lindenhof</h2>
      <p class="intro">In reizvoller Landschaft zwischen Schwarzwald, Bodensee, Schwäbischer Alb und Donautal liegt die kleine und lebendige Stadt Talbrunn. Hier bauen wir für Sie die "Wohnresidenz am Lindenhof": zwei hoch energieeffiziente Wohnhäuser mit FEB55 Standard und insgesamt 19 exklusiv ausgestatteten Wohnungen, umgeben von schönen Grünflächen und attraktiven Möglichkeiten für Einkauf und Freizeit im Nahbereich.</p>
      <p class="tagline">Geben Sie Ihre Träume in unsere Hände.</p>
    </div>
    <div class="navy-left"></div>
    <div class="ph ph-house big" role="img" aria-label="Außenansicht der Wohnanlage"></div>
    <div class="ph ph-room s1" role="img" aria-label="Schlafzimmer"></div>
    <div class="ph ph-room s2" role="img" aria-label="Moderne Küche"></div>
    <div class="ph ph-room wide" role="img" aria-label="Wohnzimmer mit Essbereich"></div>
    <p class="claim">Wir definieren Wohnen neu.</p>
  </div>
  <div class="panel-mid">
    <div class="mid-copy">
      <h2 class="title">Sie haben die Wahl!</h2>
      <p class="intro">Die 19 Wohnungen der Wohnresidenz am Lindenhof bestehen aus 2 bis 4 Zimmern und sind von ca. 60 bis 160 Quadratmeter groß. Damit bietet das moderne Wohnprojekt geeigneten Wohnraum für Singles, für Pärchen sowie für Familien mit Kindern.</p>
    </div>
    <div class="ph ph-bedroom" role="img" aria-label="Schlafzimmer und offener Wohnbereich"></div>
    <div class="row" style="top:133px">
      <div class="col a"><div class="bar">Penthouse<span class="letter">A</span></div><div class="plan" role="img" aria-label="Grundriss Penthouse Haus A"><span class="tag sold" style="left:70px;top:8px">Verkauft</span></div><div class="nums"><span>107</span><span>108</span></div><div class="units"><p class="unit"><span class="name">Wohnung 107</span>~ 147,49 m²<br>987.654,32 €</p><p class="unit"><span class="name">Wohnung 108</span>~ 143,41 m²<br><span class="st">Verkauft</span></p></div></div>
      <div class="col b"><div class="bar">Penthouse<span class="letter">B</span></div><div class="plan out-orange" role="img" aria-label="Grundriss Penthouse Haus B"><span class="tag res" style="left:75px;top:12px">Reserviert</span></div><div class="nums"><span>209</span><span>210</span><span>211</span></div><div class="units"><p class="unit"><span class="name">Wohnung 209</span>~ 118,25 m²<br>987.654,32 €</p><p class="unit"><span class="name">Wohnung 210</span>~ 68,50 m²<br>987.654,32 €</p><p class="unit"><span class="name">Wohnung 211</span>~ 120,75 m²<br><span class="st">Reserviert</span></p></div></div>
    </div>
    <div class="row" style="top:299px">
      <div class="col a"><div class="bar">Obergeschoss<span class="letter">A</span></div><div class="plan" role="img" aria-label="Grundriss Obergeschoss Haus A"><span class="tag res" style="left:38px;top:92px">Reserviert</span></div><div class="nums"><span>104</span><span>105</span><span>106</span></div><div class="units"><p class="unit"><span class="name">Wohnung 104</span>~ 121,49 m²<br>987.654,32 €</p><p class="unit"><span class="name">Wohnung 105</span>~ 85,64 m²<br><span class="st">Reserviert</span></p><p class="unit"><span class="name">Wohnung 106</span>~ 123,32 m²<br>987.654,32 €</p></div></div>
      <div class="col b"><div class="bar">Obergeschoss<span class="letter">B</span></div><div class="plan" role="img" aria-label="Grundriss Obergeschoss Haus B"><span class="tag sold" style="left:82px;top:92px">Verkauft</span></div><div class="nums"><span>205</span><span>206</span><span>207</span><span>208</span></div><div class="units"><p class="unit"><span class="name">Wohnung 205</span>~ 121,49 m²<br>987.654,32 €</p><p class="unit"><span class="name">Wohnung 206</span>~ 60,20 m²<br>987.654,32 €</p><p class="unit"><span class="name">Wohnung 207</span>~ 60,20 m²<br><span class="st">Verkauft</span></p><p class="unit"><span class="name">Wohnung 208</span>~ 114,61 m²<br>987.654,32 €</p></div></div>
    </div>
    <div class="row" style="top:483px">
      <div class="col a"><div class="bar">Erdgeschoss<span class="letter">A</span></div><div class="plan" role="img" aria-label="Grundriss Erdgeschoss Haus A"><span class="tag sold" style="left:4px;top:10px">Verkauft</span></div><div class="nums"><span>101</span><span>102</span><span>103</span></div><div class="units"><p class="unit"><span class="name">Wohnung 101</span>~ 103,96 m²<br><span class="st">Verkauft</span></p><p class="unit"><span class="name">Wohnung 102</span>~ 85,64 m²<br>987.654,32 €</p><p class="unit"><span class="name">Wohnung 103</span>~ 109,02 m²<br>987.654,32 €</p></div></div>
      <div class="col b"><div class="bar">Erdgeschoss<span class="letter">B</span></div><div class="plan out-orange" role="img" aria-label="Grundriss Erdgeschoss Haus B"><span class="tag res" style="left:82px;top:10px">Reserviert</span></div><div class="nums"><span>201</span><span>202</span><span>203</span><span>204</span></div><div class="units"><p class="unit"><span class="name">Wohnung 201</span>~ 103,96 m²<br>987.654,32 €</p><p class="unit"><span class="name">Wohnung 202</span>~ 60,20 m²<br>987.654,32 €</p><p class="unit"><span class="name">Wohnung 203</span>~ 60,21 m²<br>987.654,32 €</p><p class="unit"><span class="name">Wohnung 204</span>~ 114,61 m²<br><span class="st">Reserviert</span></p></div></div>
    </div>
  </div>
  <div class="panel-right">
    <div class="ph ph-building" role="img" aria-label="Moderner Neubau mit Balkonen und Terrassen"></div>
    <div class="navy-right">
      <h2 class="title">Gründe für eine Wohnung der Wohnresidenz am Lindenhof</h2>
      <ul class="reasons">
        <li>Fenster mit Dreifachverglasung und einem optimalen Sonnenschutz</li>
        <li>Verlegung hochwertiger Bodenbeläge</li>
        <li>Fußbodenheizung mit Komfort-Einzelregelung</li>
        <li>Überhohe Türen von 2,12 m</li>
        <li>Verwendung bekannter Hersteller bei Sanitärprodukten wie Aquaris, Keramo oder Sanoro</li>
        <li>Barrierefreie, bodenebene Duschen</li>
        <li>Hochwertige Multimediastationen in jedem Wohnraum</li>
        <li>Elektrische Rollläden bzw. Jalousien</li>
        <li>Abstellmöglichkeit für 2 Fahrräder gegeben</li>
        <li>Überhohe Decken</li>
        <li>Niedrigenergiehaus als Effizienzhaus 55 gem. EnEV 2016 (ca. 45% besser als gefordert)</li>
        <li>Zinsgünstige Darlehen aufgrund FEB55 möglich (100.000.- € ab 0,75%)</li>
        <li>Staatlicher Zuschuss von 5.000.- €</li>
        <li>Barrierefreier Aufzug von der Tiefgarage bis in jede Wohnung</li>
        <li>Tiefgaragenstellplatz optional erhältlich</li>
        <li>Zukunftsweisende KNX/EIB Bus-Elektroinstallation möglich</li>
        <li>Kontrollierte Wohnraumbelüftung mit Wärmerückgewinnung in allen Wohnungen</li>
      </ul>
    </div>
    <div class="action"><h3>Aktion</h3><p>Beim Kauf einer Wohnung<br>bis zum XX.XX.XX, erhalten Sie<br>einen Bemusterungsgutschein<br>im Wert von 5.000 €.</p></div>
  </div>
</section>

<div class="variant-label" style="top:1663px">3</div>
<section class="spread" style="left:125px;top:1663px">
  <div class="panel-left">
    <div class="ph ph-town" role="img" aria-label="Luftaufnahme der Stadt Talbrunn bei Sonnenuntergang"></div>
    <div class="band"></div>
    <div class="left-copy">
      <h2 class="title">Wohnresidenz am Lindenhof</h2>
      <p class="intro">In reizvoller Landschaft zwischen Schwarzwald, Bodensee, Schwäbischer Alb und Donautal liegt die kleine und lebendige Stadt Talbrunn. Hier bauen wir für Sie die "Wohnresidenz am Lindenhof": zwei hoch energieeffiziente Wohnhäuser mit FEB55 Standard und insgesamt 19 exklusiv ausgestatteten Wohnungen, umgeben von schönen Grünflächen und attraktiven Möglichkeiten für Einkauf und Freizeit im Nahbereich.</p>
      <p class="tagline">Geben Sie Ihre Träume in unsere Hände.</p>
    </div>
    <div class="navy-left"></div>
    <div class="ph ph-house big" role="img" aria-label="Außenansicht der Wohnanlage"></div>
    <div class="ph ph-room s1" role="img" aria-label="Schlafzimmer"></div>
    <div class="ph ph-room s2" role="img" aria-label="Moderne Küche"></div>
    <div class="ph ph-room wide" role="img" aria-label="Wohnzimmer mit Essbereich"></div>
    <p class="claim">Wir definieren Wohnen neu.</p>
  </div>
  <div class="panel-mid">
    <div class="mid-copy">
      <h2 class="title">Sie haben die Wahl!</h2>
      <p class="intro">Die 19 Wohnungen der Wohnresidenz am Lindenhof bestehen aus 2 bis 4 Zimmern und sind von ca. 60 bis 160 Quadratmeter groß. Damit bietet das moderne Wohnprojekt geeigneten Wohnraum für Singles, für Pärchen sowie für Familien mit Kindern.</p>
    </div>
    <div class="ph ph-bedroom" role="img" aria-label="Schlafzimmer und offener Wohnbereich"></div>
    <div class="row" style="top:133px">
      <div class="col a"><div class="bar">Penthouse<span class="letter">A</span></div><div class="plan" role="img" aria-label="Grundriss Penthouse Haus A"><span class="tag sold" style="left:70px;top:8px">Verkauft</span></div><div class="nums"><span>107</span><span>108</span></div><div class="units"><p class="unit"><span class="name">Wohnung 107</span>~ 147,49 m²<br>987.654,32 €</p><p class="unit"><span class="name">Wohnung 108</span>~ 143,41 m²<br><span class="st">Verkauft</span></p></div></div>
      <div class="col b"><div class="bar">Penthouse<span class="letter">B</span></div><div class="plan out-orange" role="img" aria-label="Grundriss Penthouse Haus B"><span class="tag res" style="left:75px;top:12px">Reserviert</span></div><div class="nums"><span>209</span><span>210</span><span>211</span></div><div class="units"><p class="unit"><span class="name">Wohnung 209</span>~ 118,25 m²<br>987.654,32 €</p><p class="unit"><span class="name">Wohnung 210</span>~ 68,50 m²<br>987.654,32 €</p><p class="unit"><span class="name">Wohnung 211</span>~ 120,75 m²<br><span class="st">Reserviert</span></p></div></div>
    </div>
    <div class="row" style="top:299px">
      <div class="col a"><div class="bar">Obergeschoss<span class="letter">A</span></div><div class="plan" role="img" aria-label="Grundriss Obergeschoss Haus A"><span class="tag res" style="left:38px;top:92px">Reserviert</span></div><div class="nums"><span>104</span><span>105</span><span>106</span></div><div class="units"><p class="unit"><span class="name">Wohnung 104</span>~ 121,49 m²<br>987.654,32 €</p><p class="unit"><span class="name">Wohnung 105</span>~ 85,64 m²<br><span class="st">Reserviert</span></p><p class="unit"><span class="name">Wohnung 106</span>~ 123,32 m²<br>987.654,32 €</p></div></div>
      <div class="col b"><div class="bar">Obergeschoss<span class="letter">B</span></div><div class="plan" role="img" aria-label="Grundriss Obergeschoss Haus B"><span class="tag sold" style="left:82px;top:92px">Verkauft</span></div><div class="nums"><span>205</span><span>206</span><span>207</span><span>208</span></div><div class="units"><p class="unit"><span class="name">Wohnung 205</span>~ 121,49 m²<br>987.654,32 €</p><p class="unit"><span class="name">Wohnung 206</span>~ 60,20 m²<br>987.654,32 €</p><p class="unit"><span class="name">Wohnung 207</span>~ 60,20 m²<br><span class="st">Verkauft</span></p><p class="unit"><span class="name">Wohnung 208</span>~ 114,61 m²<br>987.654,32 €</p></div></div>
    </div>
    <div class="row" style="top:483px">
      <div class="col a"><div class="bar">Erdgeschoss<span class="letter">A</span></div><div class="plan" role="img" aria-label="Grundriss Erdgeschoss Haus A"><span class="tag sold" style="left:4px;top:10px">Verkauft</span></div><div class="nums"><span>101</span><span>102</span><span>103</span></div><div class="units"><p class="unit"><span class="name">Wohnung 101</span>~ 103,96 m²<br><span class="st">Verkauft</span></p><p class="unit"><span class="name">Wohnung 102</span>~ 85,64 m²<br>987.654,32 €</p><p class="unit"><span class="name">Wohnung 103</span>~ 109,02 m²<br>987.654,32 €</p></div></div>
      <div class="col b"><div class="bar">Erdgeschoss<span class="letter">B</span></div><div class="plan out-orange" role="img" aria-label="Grundriss Erdgeschoss Haus B"><span class="tag res" style="left:82px;top:10px">Reserviert</span></div><div class="nums"><span>201</span><span>202</span><span>203</span><span>204</span></div><div class="units"><p class="unit"><span class="name">Wohnung 201</span>~ 103,96 m²<br>987.654,32 €</p><p class="unit"><span class="name">Wohnung 202</span>~ 60,20 m²<br>987.654,32 €</p><p class="unit"><span class="name">Wohnung 203</span>~ 60,21 m²<br>987.654,32 €</p><p class="unit"><span class="name">Wohnung 204</span>~ 114,61 m²<br><span class="st">Reserviert</span></p></div></div>
    </div>
  </div>
  <div class="panel-right">
    <div class="ph ph-building" role="img" aria-label="Moderner Neubau mit Balkonen und Terrassen"></div>
    <div class="navy-right">
      <h2 class="title">Gründe für eine Wohnung der Wohnresidenz am Lindenhof</h2>
      <ul class="reasons">
        <li>Fenster mit Dreifachverglasung und einem optimalen Sonnenschutz</li>
        <li>Verlegung hochwertiger Bodenbeläge</li>
        <li>Fußbodenheizung mit Komfort-Einzelregelung</li>
        <li>Überhohe Türen von 2,12 m</li>
        <li>Verwendung bekannter Hersteller bei Sanitärprodukten wie Aquaris, Keramo oder Sanoro</li>
        <li>Barrierefreie, bodenebene Duschen</li>
        <li>Hochwertige Multimediastationen in jedem Wohnraum</li>
        <li>Elektrische Rollläden bzw. Jalousien</li>
        <li>Abstellmöglichkeit für 2 Fahrräder gegeben</li>
        <li>Überhohe Decken</li>
        <li>Niedrigenergiehaus als Effizienzhaus 55 gem. EnEV 2016 (ca. 45% besser als gefordert)</li>
        <li>Zinsgünstige Darlehen aufgrund FEB55 möglich (100.000.- € ab 0,75%)</li>
        <li>Staatlicher Zuschuss von 5.000.- €</li>
        <li>Barrierefreier Aufzug von der Tiefgarage bis in jede Wohnung</li>
        <li>Tiefgaragenstellplatz optional erhältlich</li>
        <li>Zukunftsweisende KNX/EIB Bus-Elektroinstallation möglich</li>
        <li>Kontrollierte Wohnraumbelüftung mit Wärmerückgewinnung in allen Wohnungen</li>
      </ul>
    </div>
    <div class="action"><h3>Aktion</h3><p>Beim Kauf einer Wohnung<br>bis zum XX.XX.XX, erhalten Sie<br>einen Bemusterungsgutschein<br>im Wert von 5.000 €.</p></div>
  </div>
</section>

<div class="variant-label" style="top:2428px">4</div>
<section class="spread v4" style="left:125px;top:2428px">
  <div class="panel-left">
    <div class="ph ph-town" role="img" aria-label="Luftaufnahme der Stadt Talbrunn bei Sonnenuntergang"></div>
    <div class="band"></div>
    <div class="left-copy">
      <h2 class="title">Wohnresidenz am Lindenhof</h2>
      <p class="intro">In reizvoller Landschaft zwischen Schwarzwald, Bodensee, Schwäbischer Alb und Donautal liegt die kleine und lebendige Stadt Talbrunn. Hier bauen wir für Sie die "Wohnresidenz am Lindenhof": zwei hoch energieeffiziente Wohnhäuser mit FEB55 Standard und insgesamt 19 exklusiv ausgestatteten Wohnungen, umgeben von schönen Grünflächen und attraktiven Möglichkeiten für Einkauf und Freizeit im Nahbereich.</p>
      <p class="tagline">Geben Sie Ihre Träume in unsere Hände.</p>
    </div>
    <div class="navy-left"></div>
    <div class="ph ph-house big" role="img" aria-label="Außenansicht der Wohnanlage"></div>
    <div class="ph ph-room s1" role="img" aria-label="Schlafzimmer"></div>
    <div class="ph ph-room s2" role="img" aria-label="Moderne Küche"></div>
    <div class="ph ph-room wide" role="img" aria-label="Wohnzimmer mit Essbereich"></div>
    <p class="claim">Wir definieren Wohnen neu.</p>
  </div>
  <div class="panel-mid">
    <div class="mid-copy">
      <h2 class="title">Sie haben die Wahl!</h2>
      <p class="intro">Die 19 Wohnungen der Wohnresidenz am Lindenhof bestehen aus 2 bis 4 Zimmern und sind von ca. 60 bis 160 Quadratmeter groß. Damit bietet das moderne Wohnprojekt geeigneten Wohnraum für Singles, für Pärchen sowie für Familien mit Kindern.</p>
    </div>
    <div class="ph ph-bedroom" role="img" aria-label="Schlafzimmer und offener Wohnbereich"></div>
    <div class="row" style="top:133px">
      <div class="col a"><div class="bar">Penthouse<span class="letter">A</span></div><div class="plan" role="img" aria-label="Grundriss Penthouse Haus A"><span class="tag sold" style="left:70px;top:8px">Verkauft</span></div><div class="nums"><span>107</span><span>108</span></div><div class="units"><p class="unit"><span class="name">Wohnung 107</span>~ 147,49 m²<br>987.654,32 €</p><p class="unit"><span class="name">Wohnung 108</span>~ 143,41 m²<br><span class="st">Verkauft</span></p></div></div>
      <div class="col b"><div class="bar">Penthouse<span class="letter">B</span></div><div class="plan out-orange" role="img" aria-label="Grundriss Penthouse Haus B"><span class="tag res" style="left:75px;top:12px">Reserviert</span></div><div class="nums"><span>209</span><span>210</span><span>211</span></div><div class="units"><p class="unit"><span class="name">Wohnung 209</span>~ 118,25 m²<br>987.654,32 €</p><p class="unit"><span class="name">Wohnung 210</span>~ 68,50 m²<br>987.654,32 €</p><p class="unit"><span class="name">Wohnung 211</span>~ 120,75 m²<br><span class="st">Reserviert</span></p></div></div>
    </div>
    <div class="row" style="top:299px">
      <div class="col a"><div class="bar">Obergeschoss<span class="letter">A</span></div><div class="plan" role="img" aria-label="Grundriss Obergeschoss Haus A"><span class="tag res" style="left:38px;top:92px">Reserviert</span></div><div class="nums"><span>104</span><span>105</span><span>106</span></div><div class="units"><p class="unit"><span class="name">Wohnung 104</span>~ 121,49 m²<br>987.654,32 €</p><p class="unit"><span class="name">Wohnung 105</span>~ 85,64 m²<br><span class="st">Reserviert</span></p><p class="unit"><span class="name">Wohnung 106</span>~ 123,32 m²<br>987.654,32 €</p></div></div>
      <div class="col b"><div class="bar">Obergeschoss<span class="letter">B</span></div><div class="plan" role="img" aria-label="Grundriss Obergeschoss Haus B"><span class="tag sold" style="left:82px;top:92px">Verkauft</span></div><div class="nums"><span>205</span><span>206</span><span>207</span><span>208</span></div><div class="units"><p class="unit"><span class="name">Wohnung 205</span>~ 121,49 m²<br>987.654,32 €</p><p class="unit"><span class="name">Wohnung 206</span>~ 60,20 m²<br>987.654,32 €</p><p class="unit"><span class="name">Wohnung 207</span>~ 60,20 m²<br><span class="st">Verkauft</span></p><p class="unit"><span class="name">Wohnung 208</span>~ 114,61 m²<br>987.654,32 €</p></div></div>
    </div>
    <div class="row" style="top:483px">
      <div class="col a"><div class="bar">Erdgeschoss<span class="letter">A</span></div><div class="plan" role="img" aria-label="Grundriss Erdgeschoss Haus A"><span class="tag sold" style="left:4px;top:10px">Verkauft</span></div><div class="nums"><span>101</span><span>102</span><span>103</span></div><div class="units"><p class="unit"><span class="name">Wohnung 101</span>~ 103,96 m²<br><span class="st">Verkauft</span></p><p class="unit"><span class="name">Wohnung 102</span>~ 85,64 m²<br>987.654,32 €</p><p class="unit"><span class="name">Wohnung 103</span>~ 109,02 m²<br>987.654,32 €</p></div></div>
      <div class="col b"><div class="bar">Erdgeschoss<span class="letter">B</span></div><div class="plan out-orange" role="img" aria-label="Grundriss Erdgeschoss Haus B"><span class="tag res" style="left:82px;top:10px">Reserviert</span></div><div class="nums"><span>201</span><span>202</span><span>203</span><span>204</span></div><div class="units"><p class="unit"><span class="name">Wohnung 201</span>~ 103,96 m²<br>987.654,32 €</p><p class="unit"><span class="name">Wohnung 202</span>~ 60,20 m²<br>987.654,32 €</p><p class="unit"><span class="name">Wohnung 203</span>~ 60,21 m²<br>987.654,32 €</p><p class="unit"><span class="name">Wohnung 204</span>~ 114,61 m²<br><span class="st">Reserviert</span></p></div></div>
    </div>
  </div>
  <div class="panel-right">
    <div class="ph ph-building" role="img" aria-label="Moderner Neubau mit Balkonen und Terrassen"></div>
    <div class="navy-right">
      <h2 class="title">Gründe für eine Wohnung der Wohnresidenz am Lindenhof</h2>
      <ul class="reasons">
        <li>Fenster mit Dreifachverglasung und einem optimalen Sonnenschutz</li>
        <li>Verlegung hochwertiger Bodenbeläge</li>
        <li>Fußbodenheizung mit Komfort-Einzelregelung</li>
        <li>Überhohe Türen von 2,12 m</li>
        <li>Verwendung bekannter Hersteller bei Sanitärprodukten wie Aquaris, Keramo oder Sanoro</li>
        <li>Barrierefreie, bodenebene Duschen</li>
        <li>Hochwertige Multimediastationen in jedem Wohnraum</li>
        <li>Elektrische Rollläden bzw. Jalousien</li>
        <li>Abstellmöglichkeit für 2 Fahrräder gegeben</li>
        <li>Überhohe Decken</li>
        <li>Niedrigenergiehaus als Effizienzhaus 55 gem. EnEV 2016 (ca. 45% besser als gefordert)</li>
        <li>Zinsgünstige Darlehen aufgrund FEB55 möglich (100.000.- € ab 0,75%)</li>
        <li>Staatlicher Zuschuss von 5.000.- €</li>
        <li>Barrierefreier Aufzug von der Tiefgarage bis in jede Wohnung</li>
        <li>Tiefgaragenstellplatz optional erhältlich</li>
        <li>Zukunftsweisende KNX/EIB Bus-Elektroinstallation möglich</li>
        <li>Kontrollierte Wohnraumbelüftung mit Wärmerückgewinnung in allen Wohnungen</li>
      </ul>
    </div>
    <div class="action"><h3>Aktion</h3><p>Beim Kauf einer Wohnung<br>bis zum XX.XX.XX, erhalten Sie<br>einen Bemusterungsgutschein<br>im Wert von 5.000 €.</p></div>
  </div>
</section>

</body>
</html>
```